redesign "Advertise Now Page"

Please check out the website ZUVRIDOKS.com and see the following page that I would like to redesign:

http://www.zuvridoks.com/listings/sellplates

OBJECTIVES:
1 - Convert more traffic into conversions
2 - To get key messages across about what we can provide
2 - Advertising Options to be Clear and Concise
3 - Information points to show detailed information

See attached information for detailed specifications

Reason: I requested that two designs merge into two but this has not happened yet. Waiting for revisions.

Target Market(s)

90% Male

Requirements
Must have
• Professionally designed and developed to a very high standard and within the current existing design as possible.

Please see http://www.draftloom.example/publish/5019372/ for something that I have thought of as a mock up but please be aware that you are free to experiment.

I also kind of like these vector images so something like that which is matched to my website would be excellent.

http://www.vectorbarn.example/pic-40938217/stock-vector-web-banner-elements-for-web-templete-design-used.html
http://www.vectorbarn.example/pic-52817460/stock-vector-clean-web-boxes.html
http://www.vectorbarn.example/pic-63190274/stock-vector-web-elements-for-hosting.html
http://www.vectorbarn.example/pic-18472936/stock-vector-vector-pricing-table-template.html
http://www.vectorbarn.example/pic-37605182/stock-vector-design-elements-for-price-list-or-web-banner.html

```html
<!DOCTYPE html>
<html lang="en">
<head>
<meta charset="utf-8">
<title>Zuvridoks – Advertise Now</title>
<link href="https://fonts.googleapis.com/css2?family=Open+Sans:wght@400;600;700;800&family=Oswald:wght@500;700&display=swap" rel="stylesheet">
<style>
:root{
  --black:#050505;
  --orange:#f7a000;
  --orange-light:#ffc62a;
  --orange-dark:#e48a00;
  --yellow:#ffe400;
  --magenta:#e0188c;
  --pink:#ff2ea6;
  --grey-bg:#ececec;
  --grey-panel:#f4f4f4;
  --grey-line:#d2d2d2;
  --grey-btn:#b9b9b9;
  --text:#333;
  --text-soft:#666;
  --white:#fff;
  --red:#e0101a;
  --plate:#ffd200;
}
*{box-sizing:border-box;margin:0;padding:0}
html,body{width:1200px;height:2840px;overflow:hidden;background:var(--white)}
body{font-family:"Open Sans",Arial,sans-serif;color:var(--text)}
.page{position:absolute;left:47px;top:0;width:1106px;height:2840px}
.abs{position:absolute}

/* header */
.site-header{left:0;top:19px;width:1106px;height:293px;background:var(--black);border-radius:12px 12px 0 0}
.top-links{left:37px;top:16px;display:flex;gap:24px;font-size:13px;color:var(--white)}
.brand{left:42px;top:92px;display:flex;align-items:center;gap:12px}
.brand-dot{width:34px;height:34px;border-radius:50%;background:var(--red)}
.brand-name{font-size:60px;font-weight:800;color:var(--white);letter-spacing:-1px;line-height:1}
.tagline{left:44px;top:170px;font-size:11px;color:var(--yellow);font-weight:600}
.sponsor{left:440px;top:38px;width:360px;text-align:center;font-family:"Oswald",sans-serif;line-height:1}
.sponsor .lead{color:var(--yellow);font-size:20px;font-weight:500}
.sponsor .title{color:var(--white);font-size:58px;font-weight:700;margin-top:4px}
.sponsor .at{color:var(--yellow);font-size:18px;font-weight:500;margin-top:2px}
.sponsor .event{color:var(--pink);font-size:40px;font-weight:700;margin-top:2px}
.sponsor .year{color:var(--yellow);font-size:40px;font-weight:700;margin-top:2px}
.award-badge{left:810px;top:8px;width:280px;height:230px}
.main-tabs{left:50px;top:250px;display:flex;gap:5px}
.tab{height:43px;padding:0 14px;border-radius:10px 10px 0 0;background:linear-gradient(var(--orange-light),var(--orange));color:var(--white);font-size:15px;font-weight:700;display:flex;align-items:center}
.tab.is-active{background:linear-gradient(#fff,#ddd);color:#444}
.sub-nav{left:0;top:312px;width:1106px;height:38px;background:linear-gradient(var(--orange-light),var(--orange));display:flex;align-items:center;padding-left:48px;font-size:12px;font-weight:700;color:#3a2a00;gap:8px}

/* hero */
.hero{left:0;top:352px;width:1106px;height:398px;background:linear-gradient(#f6f6f6,#e2e2e2)}
.hero-photo{left:0;top:363px;width:743px;height:382px;background:linear-gradient(180deg,#5f4a36 0%,#8b6f50 40%,#a7a39c 70%,#8d8b88 100%)}
.callout{left:757px;top:363px;width:345px;height:300px;background:linear-gradient(var(--orange-light),var(--orange-dark));text-align:center;color:#222;padding-top:16px}
.callout::after{content:"";position:absolute;left:40px;bottom:-28px;border-left:0 solid transparent;border-right:36px solid transparent;border-top:28px solid var(--orange-dark)}
.callout .big{font-size:44px;font-weight:600;line-height:1.05}
.callout .sub{font-size:26px;line-height:1.15;margin-top:14px}
.callout .price{font-size:64px;font-weight:800;color:var(--white);line-height:1.1;margin-top:12px}
.callout .from{font-size:20px;color:var(--white)}
.callout-tab{left:845px;top:663px;width:200px;height:38px;background:linear-gradient(#fff,#e4e4e4);font-size:16px;display:flex;align-items:center;justify-content:center;color:#444;box-shadow:0 4px 6px rgba(0,0,0,.15)}

/* sell */
.sell{left:0;top:773px;width:1106px;height:188px;background:linear-gradient(#fff,#e6e6e6);box-shadow:0 2px 6px rgba(0,0,0,.2);padding:30px 34px}
.sell h1{font-size:30px;font-weight:700;color:#3a3a3a;letter-spacing:.2px}
.sell p{font-size:14px;line-height:22px;color:var(--text-soft);margin-top:8px}
.sell-tab{left:90px;top:961px;width:170px;height:40px;background:linear-gradient(#fff,#e8e8e8);font-size:16px;color:#444;display:flex;align-items:center;padding-left:12px;box-shadow:0 3px 5px rgba(0,0,0,.12)}
.sell-tab::before{content:"";position:absolute;left:0;top:-20px;border-right:24px solid transparent;border-bottom:20px solid #fff}

/* pricing */
.plan{background:linear-gradient(#fff,#ededed);box-shadow:0 2px 8px rgba(0,0,0,.15);text-align:center}
.plan .ribbon{position:absolute;left:50%;transform:translateX(-50%);top:-2px;width:150px;height:40px;border-radius:4px;font-size:24px;display:flex;align-items:center;justify-content:center}
.plan .price-box{position:absolute;left:28px;right:28px;border-radius:6px;background:linear-gradient(var(--orange-light),var(--orange-dark));color:var(--white);padding-top:6px}
.plan .price-box b{display:block;font-size:54px;font-weight:800;line-height:1.1}
.plan .price-box span{font-size:18px}
.plan ul{position:absolute;left:0;right:0;list-style:none;font-size:11px;color:#666;line-height:31px}
.plan .buy{position:absolute;left:50%;transform:translateX(-50%);bottom:6px;width:135px;height:34px;background:var(--grey-btn);color:var(--white);font-size:15px;display:flex;align-items:center;justify-content:center}
.bronze .ribbon{background:linear-gradient(#d6d2a6,#a9a36a);color:#4a4620}
.silver .ribbon{background:linear-gradient(#fafafa,#d4d4d4);color:#555}
.gold .ribbon{background:linear-gradient(#f9d76a,#e2a92a);color:#5a3b00}

/* comparison */
.compare{left:0;top:1500px;width:1106px;height:48px;background:linear-gradient(#f3f3f3,#dcdcdc);font-size:21px;font-weight:700;color:#333;display:flex;align-items:center;padding-left:16px}
.unhide{left:940px;top:1548px;width:140px;height:36px;background:linear-gradient(#fff,#e6e6e6);font-size:15px;color:#444;display:flex;align-items:center;padding-left:34px}
.unhide::after{content:"";position:absolute;right:-26px;top:-48px;border-left:26px solid #e6e6e6;border-bottom:48px solid transparent}

/* facts */
.facts{left:0;top:1613px;width:1106px;height:485px;background:var(--grey-bg)}
.section-title{font-size:20px;font-weight:700;color:#333}
.fact-orange{background:linear-gradient(var(--orange-light),var(--orange-dark));box-shadow:0 3px 6px rgba(0,0,0,.2);text-align:center;color:#4a2a00;display:flex;flex-direction:column;justify-content:center}
.fact-orange.profit{font-size:28px;font-weight:600;line-height:1.25}
.fact-orange.search{font-size:17px;font-weight:600;line-height:1.3;color:#222}
.search-names{display:flex;justify-content:center;gap:14px;font-size:30px;font-weight:700;color:#1c3f94;margin-bottom:14px}
.card-white{background:var(--white);padding:22px 20px}
.card-white h3{font-size:21px;font-weight:700;color:#333;margin-bottom:14px}
.card-white p{font-size:14px;line-height:21px;color:#555}
.why p{font-size:13.5px;line-height:24.6px;color:#555;text-align:justify;margin-top:12px}

/* plates */
.plate-card{top:2128px;width:264px;height:190px;background:linear-gradient(#fff,#e9e9e9);box-shadow:0 2px 6px rgba(0,0,0,.18);padding:14px 16px;font-size:12px}
.plate{margin:0 auto;width:160px;height:36px;background:var(--plate);border:2px solid #222;border-radius:4px;font-family:"Oswald",sans-serif;font-size:24px;font-weight:700;color:#111;display:flex;align-items:center;justify-content:center;letter-spacing:1px}
.plate-card .user{color:var(--orange);font-size:14px;margin-top:20px}
.plate-card .meta{display:flex;justify-content:space-between;color:#555;margin-top:18px}
.plate-card .offer{font-weight:700;font-size:15px;color:#222;margin-top:2px}
.plate-card .vote{position:absolute;left:50%;transform:translateX(-50%);bottom:4px;width:110px;height:26px;background:var(--grey-btn);color:var(--white);font-size:12px;display:flex;align-items:center;justify-content:center}

/* footer */
.footer-rule{left:0;top:2327px;width:1106px;height:8px;background:var(--orange)}
.site-footer{left:0;top:2337px;width:1106px;height:441px;background:var(--black)}
.footer-col{top:2384px;width:200px;list-style:none}
.footer-col li{font-size:12.5px;color:var(--white);height:37px;line-height:36px;border-bottom:1px solid #444}
.newsletter{left:762px;top:2347px;width:344px;height:296px;background:#1a1a1a}
.newsletter-tab{left:785px;top:2349px;width:260px;height:40px;background:linear-gradient(#fff,#d9d9d9);font-size:16px;color:#333;display:flex;align-items:center;justify-content:center;letter-spacing:.5px}
.radio{left:790px;display:flex;align-items:center;gap:10px;color:var(--white);font-size:13px}
.radio i{width:14px;height:14px;border-radius:50%;background:var(--white);border:3px solid #ddd}
.radio i.on{border:4px solid #444}
.email{left:790px;top:2512px;width:198px;height:34px;background:var(--white);font-size:13px;color:#333;display:flex;align-items:center;padding-left:10px}
.submit{left:994px;top:2512px;width:78px;height:34px;background:var(--orange);color:var(--white);font-size:14px;font-weight:700;display:flex;align-items:center;justify-content:center}
.pay-box{left:790px;top:2562px;width:282px;height:66px;background:var(--white);padding:6px 10px}
.pay-name{font-size:18px;font-weight:700;color:#1c3f94}
.pay-cards{display:flex;gap:6px;margin-top:4px}
.pay-cards span{width:40px;height:22px;border-radius:3px;background:#c9c9c9}
.footer-links{left:0;top:2680px;width:1106px;text-align:center;font-size:12.5px;color:var(--white)}
.copyright{left:0;top:2716px;width:1106px;text-align:center;font-size:11px;color:#ccc}
.disclaimer{left:0;top:2748px;width:1106px;text-align:center;font-size:11px;color:#ccc}
</style>
</head>
<body>
<div class="page">

  <header class="site-header abs"></header>
  <nav class="top-links abs" style="top:35px"><span>About</span><span>Links</span><span>FAQ</span><span>Feedback</span><span>Contact</span><span>Sign In</span></nav>
  <div class="brand abs"><span class="brand-dot"></span><span class="brand-name">zuvridoks</span></div>
  <div class="tagline abs" style="top:189px">#1 for Advertising &amp; Selling "Asian Number Plates" in the UK...</div>
  <div class="sponsor abs">
    <div class="lead">is proud to be sponsoring</div>
    <div class="title">Best Single</div>
    <div class="at">at the</div>
    <div class="event">Sunline Asia</div>
    <div class="event">Music Awards</div>
    <div class="year">2011</div>
  </div>
  <svg class="award-badge abs" viewBox="0 0 280 230" role="img" aria-label="Music awards partner badge">
    <circle cx="160" cy="110" r="90" fill="#e0188c"/>
  </svg>
  <nav class="main-tabs abs" style="top:269px">
    <span class="tab">Home</span><span class="tab is-active">Advertise Now</span><span class="tab">Search</span><span class="tab">Sold Plates</span>
  </nav>
  <nav class="sub-nav abs">WANTED PLATES <span>|</span> PLATE DESIGNER <span>|</span> GALLERY <span>|</span> BLOGS <span>|</span> LOG IN <span>|</span> REGISTER</nav>

  <section class="hero abs"></section>
  <div class="hero-photo abs" role="img" aria-label="Photo of a red sports car parked in front of an old brick inn"></div>
  <div class="callout abs">
    <div class="big">Advertise<br>Until Sold</div>
    <div class="sub">No Hidden Fees<br>No Commission</div>
    <div class="price">£50</div>
    <div class="from">Listing Starting From</div>
  </div>
  <div class="callout-tab abs">Advertise Now</div>

  <section class="sell abs">
    <h1>SELL YOUR PRSONALISED NIMBER PLATES NOW</h1>
    <p>Every day Customers advertise their private palates on our homepage. This provides them with maximum exposure, providing quality enquiries and allows others to comment and rate your number plate... and now you can take advantage of this too. with www.zuvridoks.com you will be able to make a clean profit on your investment number plate - and you will do it conveniently and quickly...</p>
  </section>
  <div class="sell-tab abs">Advertise Now</div>

  <article class="plan bronze abs" style="left:0;top:1066px;width:345px;height:422px">
    <div class="ribbon">Bronze</div>
    <div class="price-box" style="top:66px;height:98px"><b>£50</b><span>Listing Starting From</span></div>
    <ul style="top:190px"><li>STANDARD LISTING AFTER 60 DAYS</li><li>ONE OFF FEE</li><li>ADVERTISE UNTIL SOLD</li><li>NO COMMISSION TAKEN</li><li>ONLINE STATS</li></ul>
    <div class="buy">Buy Now</div>
  </article>
  <article class="plan silver abs" style="left:377px;top:1027px;width:350px;height:461px">
    <div class="ribbon">Silver</div>
    <div class="price-box" style="top:70px;height:98px"><b>£50</b><span>Listing Starting From</span></div>
    <ul style="top:180px;line-height:25px"><li>SMALL PREMIUM LISTING (SCROLL)</li><li>NEWSLETTER OPTIONS</li><li>STANDARD LISTING AFTER 60 DAYS</li><li>ONE OFF FEE</li><li>ADVERTISE UNTIL SOLD</li><li>NO COMMISSION TAKEN</li><li>ONLINE STATS</li><li>SOCIAL MEDIA (Chatterly &amp; Flitter)</li><li>TOP OF SEARCH ENGINES FOR KEYWORDS</li></ul>
    <div class="buy">Buy Now</div>
  </article>
  <article class="plan gold abs" style="left:757px;top:973px;width:347px;height:515px">
    <div class="ribbon">Gold</div>
    <div class="price-box" style="top:70px;height:105px"><b>£50</b><span>Listing Starting From</span></div>
    <ul style="top:200px;line-height:32px"><li>LARGE PREMIUM LISTING (EVERY PAGE)</li><li>PLATE ADDED TO NEWSLETTER</li><li>MOBILE ADVERTISING OPTIONS</li><li>SMALL PREMIUM LISTING (SCROLL)</li><li>NEWSLETTER OPTIONS</li><li>STANDARD LISTING AFTER 60 DAYS</li><li>ONE OFF FEE</li></ul>
    <div class="buy">Buy Now</div>
  </article>

  <div class="compare abs">COMPARISON TABLE</div>
  <div class="unhide abs">Unhide</div>

  <section class="facts abs"></section>
  <h2 class="section-title abs" style="left:20px;top:1628px">THE FACTS</h2>
  <div class="fact-orange profit abs" style="left:23px;top:1664px;width:286px;height:211px">J46 Dev Plate<br>£36,000<br>Profit</div>
  <div class="card-white abs" style="left:340px;top:1664px;width:293px;height:200px">
    <h3>Testimonials</h3>
    <p>Lorem Ipsum is simply dummy text of the printing and typesetting industry. Lorem Ipsum has been the industry's standard dummy text ever since the 1500s.</p>
  </div>
  <div class="card-white abs" style="left:23px;top:1887px;width:288px;height:187px">
    <h3>Testimonials</h3>
    <p>Lorem Ipsum is simply dummy text of the printing and typesetting industry. Lorem Ipsum has been the industry's standard dummy text ever since the 1500s,</p>
  </div>
  <div class="fact-orange search abs" style="left:340px;top:1882px;width:288px;height:192px">
    <div class="search-names"><span>Searchly</span><span>Findoo</span></div>
    Top of Searchly &amp; Findoo<br>For Asian Number Plates
  </div>
  <div class="why abs" style="left:668px;top:1628px;width:436px">
    <h2 class="section-title">WHY US</h2>
    <p>Lorem Ipsum is simply dummy text of the printing and typesetting industry. Lorem Ipsum has been the industry's standard dummy text ever since the 1500s, when an unknown printer took a galley of type and scrambled it to make a type specimen book. It has survived not only five centuries, but also the leap into electronic typesetting, remaining essentially unchanged. It was popularised in the 1960s with the release of Dryset sheets containing Lorem Ipsum passages, and more recently with desktop publishing software like Quillset Layout including versions of Lorem Ipsum. Lorem Ipsum is simply dummy text of the printing and typesetting industry. Lorem Ipsum has been the industry's standard dummy text ever since the 1500s, when an unknown printer</p>
  </div>

  <article class="plate-card abs" style="left:5px"><div class="plate">DE51 JAM</div><div class="user">GUVS Sikh</div><div class="meta"><span>23/07/2011</span><span>Views(548)</span></div><div class="offer">Make me an Offer Please</div><div class="vote">Vote Now</div></article>
  <article class="plate-card abs" style="left:284px"><div class="plate">DE51 JAM</div><div class="user">GUVS Sikh</div><div class="meta"><span>23/07/2011</span><span>Views(548)</span></div><div class="offer">Make me an Offer Please</div><div class="vote">Vote Now</div></article>
  <article class="plate-card abs" style="left:558px"><div class="plate">DE51 JAM</div><div class="user">GUVS Sikh</div><div class="meta"><span>23/07/2011</span><span>Views(548)</span></div><div class="offer">Make me an Offer Please</div><div class="vote">Vote Now</div></article>
  <article class="plate-card abs" style="left:832px"><div class="plate">DE51 JAM</div><div class="user">GUVS Sikh</div><div class="meta"><span>23/07/2011</span><span>Views(548)</span></div><div class="offer">Make me an Offer Please</div><div class="vote">Vote Now</div></article>

  <div class="footer-rule abs"></div>
  <footer class="site-footer abs"></footer>
  <ul class="footer-col abs" style="left:51px"><li>UK Number Plates For Sale</li><li>Sikh Number Plates For Sale</li><li>Muslim Number Plates For Sale</li><li>Hindu Number Plates For Sale</li><li>Chinese Number Plates For Sale</li><li>Japanese Number Plates For Sale</li><li>Number Plates For Sale</li></ul>
  <ul class="footer-col abs" style="left:300px"><li>Home</li><li>About Us</li><li>Links</li><li>FAQ</li><li>Feedback</li><li>Contact Us</li></ul>
  <ul class="footer-col abs" style="left:525px"><li>Sign In</li><li>Register</li><li>Sell Your Number Plates</li><li>Plates for Sale</li><li>Wanted Plates</li><li>Plate Designer</li><li>Gallery</li></ul>

  <div class="newsletter abs"></div>
  <div class="newsletter-tab abs">JOIN OUR NEWSLETTER</div>
  <div class="radio abs" style="top:2412px"><i></i>Weekly</div>
  <div class="radio abs" style="top:2446px"><i class="on"></i>Monthly</div>
  <div class="radio abs" style="top:2480px"><i></i>Quarterly</div>
  <div class="email abs">Type Your Email Address</div>
  <div class="submit abs">Submit</div>
  <div class="pay-box abs">
    <div class="pay-name">Paynest</div>
    <div class="pay-cards"><span></span><span></span><span></span><span></span><span></span></div>
  </div>

  <nav class="footer-links abs">Home | Newsletter | Number Plate Document | NVRA Info | Car Registration Dates | Terms | Privacy | Sitemap</nav>
  <div class="copyright abs">© 2011 www.ZUVRIDOKS.com All Rights Reserved.</div>
  <div class="disclaimer abs">NVRA is a registered trade mark of the National Vehicle Registration Authority. ZUVRIDOKS is in no way affiliated to the NVRA or NVRA Personalised Registrations</div>

</div>
</body>
</html>
```